Graphic Design for Kavendra Moluthi's Yoga & Health Retreat (Pty Ltd)

Postcard flyer (and email template) for Christmas/NY mail out for a Health & Yoga Retreat

```html
<!DOCTYPE html>
<html lang="en">
<head>
<meta charset="utf-8">
<title>Yoga Retreat For Women of Color</title>
<link rel="stylesheet" href="https://fonts.googleapis.com/css2?family=Tinos&family=Delius&display=swap">
<style>
  :root {
    --panel-light: #d2306c;
    --panel-mid: #b81d55;
    --panel-dark: #8e1240;
    --ornament-bg: #f3dfe7;
    --photo-top: #d99a4a;
    --photo-bottom: #8a5a2e;
    --ink-light: #ffffff;
  }
  html, body {
    margin: 0;
    padding: 0;
    overflow: hidden;
    background: #ffffff;
  }
  .flyer {
    position: relative;
    width: 800px;
    height: 1200px;
    overflow: hidden;
    background: linear-gradient(180deg, var(--panel-light) 0%, var(--panel-mid) 45%, var(--panel-dark) 100%);
  }
  .photo-area {
    position: absolute;
    left: 0;
    top: 0;
    width: 410px;
    height: 1200px;
    background: linear-gradient(180deg, var(--photo-top) 0%, var(--photo-bottom) 100%);
  }
  .ornament-area {
    position: absolute;
    left: 270px;
    top: 0;
    width: 150px;
    height: 300px;
    background: var(--ornament-bg);
  }
  .header-band {
    position: absolute;
    left: 420px;
    top: 0;
    width: 380px;
    height: 108px;
    background: var(--panel-dark);
  }
  .presenter {
    position: absolute;
    left: 430px;
    top: 16px;
    width: 360px;
    margin: 0;
    font-family: "Tinos", "Times New Roman", serif;
    font-size: 24px;
    line-height: 1.2;
    color: var(--ink-light);
    text-align: center;
  }
  .title {
    position: absolute;
    left: 440px;
    top: 150px;
    width: 350px;
    margin: 0;
    font-family: "Delius", cursive;
    font-weight: 400;
    font-size: 44px;
    line-height: 1.3;
    color: var(--ink-light);
  }
  .title-rule {
    position: absolute;
    left: 420px;
    top: 262px;
    width: 380px;
    height: 3px;
    background: var(--ink-light);
  }
  .pitch {
    position: absolute;
    left: 425px;
    top: 400px;
    width: 360px;
    margin: 0;
    font-family: "Delius", cursive;
    font-size: 31px;
    line-height: 1.3;
    color: var(--ink-light);
    text-align: center;
  }
  .pitch-gap { display: block; height: 28px; }
  .event-date {
    position: absolute;
    left: 425px;
    top: 1000px;
    width: 360px;
    margin: 0;
    font-family: "Delius", cursive;
    font-size: 32px;
    line-height: 1.25;
    color: var(--ink-light);
    text-align: center;
  }
  .website {
    position: absolute;
    left: 425px;
    top: 1160px;
    width: 360px;
    margin: 0;
    font-family: "Delius", cursive;
    font-size: 18px;
    color: var(--ink-light);
    text-align: center;
  }
</style>
</head>
<body>
  <main class="flyer">
    <div class="photo-area" role="img" aria-label="Photo: silhouette of a woman in tree pose on rocks against an ocean sunset"></div>
    <div class="ornament-area" role="img" aria-label="Decorative magenta swirl ornament"></div>
    <div class="header-band"></div>
    <p class="presenter">Kavendra Moluthi's Yoga &amp; Health<br>Retreat (Pty Ltd)<br>Presents</p>
    <h1 class="title">Yoga Retreat For<br>Women of Color</h1>
    <div class="title-rule"></div>
    <p class="pitch">
      Enjoy the feeling of<br>peace, freedom and<br>energy that Yoga &amp;<br>meditation can provide.<br>Come for
      <span class="pitch-gap"></span>
      weekend -week and<br>learn simple and power-<br>ful ways to rejuvenate<br>you life with<br>Kavendra Moluthi.<br>All welcome.
    </p>
    <p class="event-date">October 25, 2011<br>7am -5pm</p>
    <p class="website">website www.kavendra.com.au</p>
  </main>
</body>
</html>
```